Silver Brook Home Business Cards

We need Business cards development for our expanding business. Our Company SilverBrookHome promotes grain free living through products, services and healthy living concepts. Our Products are:
Non-Grain
Non- GMO
Non- Soy
Gluten-Free

Project Deadline Extended
Reason: We will need to extend the deadline on our Business Card contest. Thanks, SBH

```html
<!DOCTYPE html>
<html lang="en">
<head>
<meta charset="utf-8">
<title>Silver Brook Home – Business Card</title>
<link rel="stylesheet" href="https://fonts.googleapis.com/css2?family=Nunito:wght@400;600;800&display=swap">
<style>
  :root {
    --backdrop: #3b1c1c;
    --card-white: #ffffff;
    --brand-green: #1d6b34;
    --deep-green: #17592b;
    --leaf-green: #8cc63f;
    --soft-grey: #e6ebe4;
    --text-light: #ffffff;
  }
  * { box-sizing: border-box; margin: 0; padding: 0; }
  html, body {
    width: 1200px; height: 800px; overflow: hidden;
    background: var(--backdrop);
    font-family: "Nunito", sans-serif;
  }
  .card {
    position: absolute; left: 75px; top: 100px;
    width: 1050px; height: 600px;
    background: var(--card-white);
    overflow: hidden;
    box-shadow: 0 20px 50px rgba(0,0,0,.45);
  }
  .card-shapes { position: absolute; inset: 0; }
  .brand {
    position: absolute; left: 90px; top: 150px;
  }
  .brand-row { display: flex; align-items: center; gap: 16px; }
  .brand-dot {
    width: 46px; height: 46px; border-radius: 50%;
    background: var(--brand-green);
  }
  .brand-name {
    font-weight: 800; font-size: 58px; line-height: 1;
    color: var(--brand-green); letter-spacing: -1px;
  }
  .brand-tagline {
    margin: 10px 0 0 64px;
    font-size: 17px; font-weight: 600; letter-spacing: 2.5px;
    color: var(--leaf-green);
  }
  .brand-tagline .suffix { font-size: 12px; margin-left: 6px; }
  .person {
    position: absolute; right: 470px; top: 420px; text-align: right;
  }
  .person-name { font-weight: 800; font-size: 34px; color: var(--text-light); }
  .person-role { font-weight: 600; font-size: 22px; color: var(--leaf-green); }
  .divider {
    position: absolute; left: 610px; top: 340px;
    width: 2px; height: 170px; background: rgba(255,255,255,.55);
  }
  .contact {
    position: absolute; left: 640px; top: 340px;
    list-style: none; color: var(--text-light);
    font-size: 25px; font-weight: 400;
  }
  .contact li { display: flex; align-items: center; gap: 14px; height: 40px; }
  .contact svg { width: 24px; height: 24px; flex: none; }
</style>
</head>
<body>
  <section class="card" aria-label="Silver Brook Home business card">
    <svg class="card-shapes" viewBox="0 0 1050 600" width="1050" height="600">
      <circle cx="250" cy="380" r="130" fill="var(--soft-grey)" role="img" aria-label="Faint brand mark decoration"/>
      <path d="M0,540 Q300,480 520,360 T1050,60 L1050,600 L0,600 Z" fill="var(--deep-green)"/>
      <path d="M560,330 Q820,170 1050,10 L1050,40 Q830,195 560,330 Z" fill="var(--leaf-green)"/>
    </svg>

    <div class="brand">
      <div class="brand-row">
        <span class="brand-dot"></span>
        <span class="brand-name">SilverBrookHome</span>
      </div>
      <p class="brand-tagline">Wisdom For Wholesome Living<span class="suffix">CO</span></p>
    </div>

    <div class="person">
      <p class="person-name">Mara Lindell</p>
      <p class="person-role">Manager</p>
    </div>

    <span class="divider"></span>

    <ul class="contact">
      <li>
        <svg viewBox="0 0 24 24" fill="var(--leaf-green)"><path d="M6.6 10.8a15 15 0 0 0 6.6 6.6l2.2-2.2c.3-.3.7-.4 1-.2 1.1.4 2.3.6 3.6.6.6 0 1 .4 1 1V20c0 .6-.4 1-1 1A17 17 0 0 1 3 4c0-.6.4-1 1-1h3.5c.6 0 1 .4 1 1 0 1.3.2 2.5.6 3.6.1.3 0 .7-.2 1z"/></svg>
        <span>1555 210 734</span>
      </li>
      <li>
        <svg viewBox="0 0 24 24" fill="var(--leaf-green)"><path d="M12 3 2 12h3v8h5v-6h4v6h5v-8h3z"/></svg>
        <span>PO Box 40918 AL 36100</span>
      </li>
      <li>
        <svg viewBox="0 0 24 24" fill="var(--leaf-green)"><path d="M3 6h18v12H3z M3 6l9 7 9-7" stroke="var(--deep-green)" stroke-width="1.5"/></svg>
        <span>info@silverbrookhome.com</span>
      </li>
      <li>
        <svg viewBox="0 0 24 24" fill="none" stroke="var(--leaf-green)" stroke-width="2"><circle cx="12" cy="12" r="9"/><path d="M3 12h18M12 3c3 3 3 15 0 18M12 3c-3 3-3 15 0 18"/></svg>
        <span>www.silverbrookhome.com</span>
      </li>
    </ul>
  </section>
</body>
</html>
```